Property risk and finance brokerage company needs a business card design

Tarlow Financial requires a business card design. Please integrate existing logo (refer uploaded file).
hex codes used on logo #002649 #008ED6 #444F51 #ADAFAA
font used - Cinzel
Contact information
Renata Sollisford
Director
Mobile: 0491 738 205
email: r.sollisford@tarlowfinancial.example.au
website: www.tarlowfinancial.example.au
CRN : 918354
PO Box 527
Kellhaven, Eastmere, 3990
Horizontal orientation please
Finance

```html
<!DOCTYPE html>
<html lang="en">
<head>
<meta charset="utf-8">
<title>Tarlow Financial – Business Card</title>
<link rel="stylesheet" href="https://fonts.googleapis.com/css2?family=Cinzel:wght@400;700&family=Cabin:wght@400&display=swap">
<style>
  :root {
    --navy: #002649;
    --sky: #008ED6;
    --slate: #444F51;
    --silver: #ADAFAA;
    --card-deep: #0f2b5f;
    --card-mid: #2a5699;
    --card-glow: #4f88d0;
    --leaf-soft: #5f93d6;
    --paper: #ffffff;
    --stage: #1c1d20;
    --ink-light: #e8eef8;
    --role-ink: #c9d6ea;
  }
  * { box-sizing: border-box; margin: 0; padding: 0; }
  html, body { width: 1200px; height: 900px; overflow: hidden; background: var(--stage); }
  .canvas { position: relative; width: 1200px; height: 900px; }

  .card {
    position: absolute;
    width: 640px;
    height: 360px;
    overflow: hidden;
    box-shadow: 0 18px 40px rgba(0,0,0,0.55);
  }

  /* Back of card */
  .card--back {
    left: 170px; top: 70px;
    background: radial-gradient(ellipse 60% 70% at 58% 45%, var(--card-glow) 0%, var(--card-mid) 45%, var(--card-deep) 100%);
  }
  .card--back .edge-band {
    position: absolute; left: 0; right: 0; height: 14px;
    background: linear-gradient(180deg, rgba(255,255,255,0.10), rgba(255,255,255,0));
  }
  .card--back .edge-band--top { top: 0; border-bottom: 1px solid rgba(150,190,240,0.35); }
  .card--back .edge-band--bottom { bottom: 0; transform: scaleY(-1); border-bottom: 1px solid rgba(150,190,240,0.3); }
  .card--back .tree-art {
    position: absolute; left: 0; top: 80px; width: 330px; height: 280px;
    background: radial-gradient(ellipse 55% 60% at 45% 45%, rgba(95,147,214,0.75) 0%, rgba(70,120,195,0.45) 55%, rgba(20,50,110,0) 85%);
  }
  .card--back .web {
    position: absolute; right: 36px; bottom: 34px;
    display: flex; align-items: center; gap: 8px;
    font-family: "Cabin", sans-serif; font-size: 17px; letter-spacing: 0.5px;
    color: var(--ink-light);
  }

  /* Front of card */
  .card--front {
    left: 390px; top: 470px;
    display: flex;
  }
  .card--front .brand-panel {
    width: 46%; background: var(--paper);
    display: flex; align-items: center; justify-content: center; gap: 14px;
  }
  .brand-mark { width: 30px; height: 30px; border-radius: 50%; background: var(--sky); flex: none; }
  .brand-name {
    font-family: "Cinzel", serif; font-weight: 400; font-size: 28px; line-height: 1.05;
    color: var(--navy);
  }
  .card--front .contact-panel {
    position: relative; flex: 1;
    background: radial-gradient(ellipse 70% 70% at 50% 30%, var(--card-glow) 0%, var(--card-mid) 45%, var(--card-deep) 100%);
    border-left: 6px solid #6d9ad6;
    padding: 84px 20px 0 34px;
    color: var(--ink-light);
  }
  .person-name {
    font-family: "Cinzel", serif; font-weight: 700; font-size: 18px; letter-spacing: 1px;
    color: #ffffff;
  }
  .person-role {
    font-family: "Cinzel", serif; font-size: 11px; letter-spacing: 1px; margin-top: 3px;
    color: var(--role-ink);
  }
  .contact-list { list-style: none; margin-top: 30px; font-family: "Cabin", sans-serif; font-size: 11px; line-height: 1.6; }
  .contact-list li { display: flex; align-items: center; gap: 7px; white-space: nowrap; }
  .contact-list .icon { width: 11px; height: 11px; flex: none; }
  .contact-list .no-icon { padding-left: 18px; }
</style>
</head>
<body>
<main class="canvas">

  <section class="card card--back" aria-label="Business card, back">
    <div class="edge-band edge-band--top"></div>
    <div class="edge-band edge-band--bottom"></div>
    <div class="tree-art" role="img" aria-label="Large decorative leafy tree in soft blues with a grey trunk"></div>
    <div class="web">
      <svg width="16" height="14" viewBox="0 0 16 14" aria-hidden="true">
        <rect x="1" y="1" width="14" height="9" rx="1" fill="#ffffff"/>
        <rect x="6" y="10" width="4" height="2" fill="#ffffff"/>
        <rect x="4" y="12" width="8" height="1.5" fill="#ffffff"/>
      </svg>
      <span>www.tarlowfinancial.example.au</span>
    </div>
  </section>

  <section class="card card--front" aria-label="Business card, front">
    <div class="brand-panel">
      <span class="brand-mark" aria-hidden="true"></span>
      <span class="brand-name">Tarlow<br>Financial</span>
    </div>
    <div class="contact-panel">
      <h1 class="person-name">Renata Sollisford</h1>
      <p class="person-role">Director</p>
      <ul class="contact-list">
        <li>
          <svg class="icon" viewBox="0 0 12 12" aria-hidden="true"><rect x="3" y="0.5" width="6" height="11" rx="1" fill="none" stroke="#fff" stroke-width="1"/><circle cx="6" cy="9.5" r="0.6" fill="#fff"/></svg>
          <span>0491 738 205</span>
        </li>
        <li>
          <svg class="icon" viewBox="0 0 12 12" aria-hidden="true"><rect x="0.5" y="2.5" width="11" height="7" fill="#fff"/><path d="M0.5 2.5 L6 7 L11.5 2.5" fill="none" stroke="#2a5699" stroke-width="1"/></svg>
          <span>r.sollisford@tarlowfinancial.example.au</span>
        </li>
        <li>
          <svg class="icon" viewBox="0 0 12 12" aria-hidden="true"><path d="M6 11.5 C3 7.5 2 6 2 4.3 A4 4 0 0 1 10 4.3 C10 6 9 7.5 6 11.5 Z" fill="#fff"/><circle cx="6" cy="4.3" r="1.5" fill="#2a5699"/></svg>
          <span>PO Box 527 - Kellhaven, Eastmere, 3990</span>
        </li>
        <li class="no-icon">Credit Rep No.: 918354</li>
      </ul>
    </div>
  </section>

</main>
</body>
</html>
```